Quillstone Business Card

We need a business card design. We have a logo from a previous Sketchfold project and I am attaching the logo files in jpeg and photoshop.

```html
<!DOCTYPE html>
<html lang="en">
<head>
<meta charset="utf-8">
<title>Quillstone Business Card</title>
<link rel="stylesheet" href="https://fonts.googleapis.com/css2?family=Open+Sans:wght@400;600;700&display=swap">
<style>
  :root {
    --backdrop: #d6d6d6;
    --card-top: #ffffff;
    --card-bottom: #ececec;
    --ink: #333333;
    --ink-soft: #4a4a4a;
    --rule: #9a9a9a;
    --brand-green: #3cb44a;
    --band-light: #bdbdbd;
    --band-dark: #4b4b4b;
  }
  * { margin: 0; padding: 0; box-sizing: border-box; }
  html, body {
    width: 1200px;
    height: 587px;
    overflow: hidden;
    background: var(--backdrop);
    font-family: "Open Sans", Arial, sans-serif;
  }
  .stage {
    position: relative;
    width: 1200px;
    height: 587px;
  }
  .business-card {
    position: absolute;
    left: 150px;
    top: 36px;
    width: 900px;
    height: 514px;
    background: linear-gradient(160deg, var(--card-top) 0%, var(--card-bottom) 100%);
    box-shadow: 0 6px 22px rgba(0, 0, 0, 0.18);
    overflow: hidden;
  }
  .card-bands {
    position: absolute;
    left: 0;
    top: 0;
    width: 900px;
    height: 514px;
  }
  .card-bands .band-light { fill: var(--band-light); }
  .card-bands .band-dark { fill: var(--band-dark); }
  .card-bands .band-green { fill: var(--brand-green); }
  .brand {
    position: absolute;
    left: 52px;
    top: 66px;
    display: flex;
    align-items: center;
    gap: 14px;
  }
  .brand-square {
    width: 34px;
    height: 34px;
    background: var(--brand-green);
  }
  .brand-name {
    font-size: 44px;
    font-weight: 700;
    color: var(--ink);
    letter-spacing: -0.5px;
    line-height: 1;
  }
  .person {
    position: absolute;
    left: 52px;
    top: 146px;
  }
  .person-name {
    font-size: 40px;
    font-weight: 400;
    color: var(--ink);
    line-height: 1.1;
  }
  .person-title {
    font-size: 28px;
    font-weight: 400;
    color: var(--brand-green);
    margin-top: 4px;
  }
  .contact-rule {
    position: absolute;
    left: 40px;
    right: 40px;
    top: 310px;
    height: 1px;
    background: var(--rule);
  }
  .contact-item {
    position: absolute;
    display: flex;
    align-items: center;
    gap: 10px;
    font-size: 18px;
    color: var(--ink-soft);
    line-height: 1.25;
    white-space: nowrap;
  }
  .contact-item svg { flex: none; fill: var(--brand-green); }
  .contact-address { left: 52px; top: 324px; align-items: flex-start; font-size: 17px; }
  .contact-email { left: 100px; top: 392px; }
  .contact-phone { left: 420px; top: 392px; }
  .contact-fax { left: 650px; top: 392px; }
  .contact-web { left: 470px; top: 432px; }
</style>
</head>
<body>
<main class="stage">
  <section class="business-card">
    <svg class="card-bands" viewBox="0 0 900 514" aria-hidden="true">
      <path class="band-light" d="M0,386 L92,386 Q106,386 112,400 L160,514 L0,514 Z"/>
      <path class="band-dark" d="M0,404 L68,404 Q82,404 88,418 L128,514 L0,514 Z"/>
      <path class="band-green" d="M560,514 L596,480 Q610,468 630,468 L900,468 L900,514 Z"/>
    </svg>

    <header class="brand">
      <span class="brand-square"></span>
      <span class="brand-name">Quillstone</span>
    </header>

    <div class="person">
      <h1 class="person-name">Evan Marsh</h1>
      <p class="person-title">Managing Director</p>
    </div>

    <div class="contact-rule"></div>

    <div class="contact-item contact-address">
      <svg width="18" height="24" viewBox="0 0 18 24"><path d="M9 0C4 0 0 4 0 9c0 6.5 9 15 9 15s9-8.5 9-15c0-5-4-9-9-9zm0 12.5A3.5 3.5 0 1 1 9 5.5a3.5 3.5 0 0 1 0 7z"/></svg>
      <span>1482 Fenwick Rd,<br>Larkdale, Virginia 22190</span>
    </div>

    <div class="contact-item contact-email">
      <svg width="26" height="18" viewBox="0 0 26 18"><path d="M0 0h26v18H0z"/><path d="M1.5 1.5L13 10l11.5-8.5" fill="none" stroke="#fff" stroke-width="2"/></svg>
      <span>evan.marsh@quillstone.com</span>
    </div>

    <div class="contact-item contact-phone">
      <svg width="28" height="22" viewBox="0 0 28 22"><path d="M2 6c0-3 5-5 12-5s12 2 12 5v2h-6V6c-2-1-10-1-12 0v2H2z"/><path d="M7 10h14l3 11H4z"/><circle cx="14" cy="15" r="3" fill="#fff"/></svg>
      <span>(555) 214 - 7730</span>
    </div>

    <div class="contact-item contact-fax">
      <svg width="28" height="22" viewBox="0 0 28 22"><path d="M8 0h12v6H8z"/><path d="M2 7h24v12H2z"/><path d="M6 15h16v7H6z" fill="#fff"/><path d="M8 17h12v1.5H8zM8 19.5h9V21H8z"/></svg>
      <span>(555) 214 - 7730</span>
    </div>

    <div class="contact-item contact-web">
      <svg width="22" height="22" viewBox="0 0 22 22"><circle cx="11" cy="11" r="10"/><path d="M1 11h20M11 1v20M11 1c-4 3-4 17 0 20M11 1c4 3 4 17 0 20M3 5.5h16M3 16.5h16" fill="none" stroke="#fff" stroke-width="1.3"/></svg>
      <span>www.quillstone.com</span>
    </div>
  </section>
</main>
</body>
</html>
```